Bref créative
BrightHollow Capital Partners
......putting entrepreneurs and investors together
Professional
Marcus Pellow
418 Weldon Avenue
Suite 340
Media, PA 19087
brighthollowcap@mailvista.net
I have selected the black & red color scheme on the logo.
Angel Investors/Angel Funds
Seed/Start-up Investment
Private Equity Funds
Venture Capital Funding
Merchant Funding
Receivable/Purchase Order Funding

```html
<!DOCTYPE html>
<html lang="en">
<head>
<meta charset="utf-8">
<title>BrightHollow Capital Partners – Business Card</title>
<link rel="stylesheet" href="https://fonts.googleapis.com/css2?family=Arimo:wght@400;700&display=swap">
<style>
  :root {
    --backdrop: #e9e7e3;
    --card: #ffffff;
    --brand-red: #e8202a;
    --ink: #1a1a1a;
    --rule-black: #111111;
    --faint-mark: #f3e3dc;
  }
  * { box-sizing: border-box; margin: 0; padding: 0; }
  html, body {
    width: 1200px;
    height: 778px;
    overflow: hidden;
    background: var(--backdrop);
    font-family: "Arimo", Arial, sans-serif;
  }
  .business-card {
    position: absolute;
    left: 110px;
    top: 109px;
    width: 980px;
    height: 560px;
    background: var(--card);
    border-radius: 40px;
    overflow: hidden;
    box-shadow: 0 6px 18px rgba(0,0,0,0.18);
  }
  .edge-band {
    position: absolute;
    left: 0; top: 0;
    width: 72px; height: 100%;
    background: var(--brand-red);
  }
  .edge-rule {
    position: absolute;
    left: 80px; top: 0;
    width: 8px; height: 100%;
    background: var(--rule-black);
  }
  .faint-mark {
    position: absolute;
    left: 700px;
    top: 250px;
    width: 250px;
    height: 250px;
    border-radius: 50%;
    background: var(--faint-mark);
    opacity: 0.7;
  }
  .wordmark {
    position: absolute;
    left: 140px;
    top: 70px;
    color: var(--ink);
    font-weight: 700;
  }
  .wordmark-name {
    display: flex;
    align-items: center;
    gap: 18px;
    font-size: 84px;
    line-height: 1;
    letter-spacing: 0.01em;
  }
  .wordmark-dot {
    width: 22px; height: 22px;
    border-radius: 50%;
    background: var(--brand-red);
  }
  .wordmark-sub {
    margin-top: 14px;
    font-size: 25px;
    letter-spacing: 0.62em;
    text-transform: uppercase;
  }
  .address {
    position: absolute;
    left: 140px;
    top: 322px;
    font-size: 24px;
    line-height: 31px;
    color: var(--ink);
    font-style: normal;
  }
  .contact-list {
    position: absolute;
    left: 140px;
    top: 400px;
    list-style: none;
    font-size: 24px;
    color: var(--ink);
  }
  .contact-list li {
    display: flex;
    align-items: center;
    gap: 10px;
    height: 34px;
  }
  .contact-icon { width: 18px; height: 18px; flex: none; }
  .holder-name {
    position: absolute;
    left: 670px;
    top: 372px;
    font-size: 28px;
    font-weight: 700;
    color: var(--brand-red);
  }
</style>
</head>
<body>
  <article class="business-card">
    <div class="edge-band"></div>
    <div class="edge-rule"></div>
    <div class="faint-mark" aria-hidden="true"></div>

    <header class="wordmark">
      <div class="wordmark-name">BrightHollow <span class="wordmark-dot"></span></div>
      <div class="wordmark-sub">Capital Partners</div>
    </header>

    <address class="address">
      418 Weldon Avenue, Suite 340<br>
      Media, PA 19087
    </address>

    <ul class="contact-list">
      <li>
        <svg class="contact-icon" viewBox="0 0 18 18" aria-label="Phone">
          <rect x="4" y="1" width="10" height="16" rx="2" fill="#e8202a"/>
          <rect x="6" y="3" width="6" height="7" fill="#fff"/>
        </svg>
        610-555-0142
      </li>
      <li>
        <svg class="contact-icon" viewBox="0 0 18 18" aria-label="Fax">
          <rect x="4" y="1" width="10" height="6" fill="#e8202a"/>
          <rect x="1" y="7" width="16" height="8" rx="2" fill="#e8202a"/>
          <rect x="4" y="11" width="10" height="6" fill="#fff" stroke="#e8202a" stroke-width="1.5"/>
        </svg>
        610-555-0187
      </li>
      <li>
        <svg class="contact-icon" viewBox="0 0 18 18" aria-label="Email">
          <rect x="1" y="3" width="16" height="12" fill="none" stroke="#e8202a" stroke-width="2"/>
          <polyline points="1,3 9,10 17,3" fill="none" stroke="#e8202a" stroke-width="2"/>
        </svg>
        brighthollowcap@mailvista.net
      </li>
    </ul>

    <p class="holder-name">Marcus Pellow</p>
  </article>
</body>
</html>
```